Radiant Crossroads - An Exciting Mission & Book Cover Project

Help me to inspire people to live their best life! This is a mission, not just a design project.
I need a Book Cover designed to keep me inspired on the process of writing my book.
Book Title: Radiant Crossroads
Tag Line: Three Simple Steps to get out of your own way, SuperCharge your Life and Step into Purpose!
Author: Marlon Teague

The three steps are: Ownership, Vision and Action (Not sure if this should be on the front or back of the book cover)

The book is a self-help, motivational book. Personal development.
The cover needs to be strong and capture peoples attention, especially with competing shelf space. I almost see a fire ball of flame or explosion that will grab peoples attention.
My company is The Summit Collective. I have added the company logo and a few pages of my presentation and topic outline to give an idea.
Maybe: The Summit Collective logo on back of the cover. website is marlonteague-example.com

THOUGHT: People should be able to take a photo of them holding the book cover showing what area of life they want Radiant Crossroads in. This is why the front cover must be so visual and powerful that they want to take a photo with it. Ie. Explosion, fire, strong and bold.

Target Market(s)

Anyone who feels stuck and needs to breakthrough and move forward in life.

Industry/Entity Type

Motivation

Font styles to use
Serif
Sans Serif

Colors
ec1f27
f37122
fbed22

Requirements
Must have
• The design must be STRONG, SIMPLE, STAND OUT ON BOOK SHELVES.
Must have an open file to swap the photo and copy out.

Back Cover Page
1) Summary
2) 2-3 testimonials. One sentence.
3) About the Author (maybe with photo)
4) Summit Collective logo
5) Website: radiantcrossroads-example.com and marlonteague-example.com
Nice to have
• If my photo works somewhere that would be great. I will change the photo later.
Added Where Does Your Compass Point? a nice cover example.
Should not have
• Right now I am writing the summary for the back of the cover. For now use Loreum Ipsum text and 2-3 recommendations. Again, I will get these only later.

```html
<!DOCTYPE html>
<html lang="en">
<head>
<meta charset="utf-8">
<title>Radiant Crossroads – Cover Spread</title>
<link rel="stylesheet" href="https://fonts.googleapis.com/css2?family=Teko:wght@500;600;700&family=Roboto:wght@400;500&display=swap">
<style>
  :root {
    --page-bg: #d4d8db;
    --ember-dark: #1f0303;
    --ember-deep: #4e0b07;
    --ember-mid: #8c1a0b;
    --flame-red: #ec1f27;
    --flame-orange: #f37122;
    --flame-yellow: #fbed22;
    --glow-light: #fff3b0;
    --ink-white: #ffffff;
    --suit-navy: #1b2848;
    --suit-shadow: #0f1730;
    --shirt-blue: #cfe0f2;
  }
  * { box-sizing: border-box; margin: 0; padding: 0; }
  html, body { width: 1200px; height: 1200px; overflow: hidden; }
  body { background: var(--page-bg); position: relative; font-family: "Roboto", sans-serif; }

  .cover-spread {
    position: absolute; left: 40px; top: 223px;
    width: 1120px; height: 754px;
    display: flex;
    box-shadow: 0 10px 30px rgba(0,0,0,.25);
  }

  .fire-art { position: absolute; inset: 0; }
  .back-cover .fire-art {
    background:
      radial-gradient(ellipse 22% 16% at 52% 57%, var(--glow-light) 0%, rgba(251,237,34,.85) 45%, transparent 100%),
      radial-gradient(ellipse 16% 12% at 30% 66%, rgba(251,237,34,.9) 0%, transparent 100%),
      radial-gradient(ellipse 16% 12% at 74% 66%, rgba(251,237,34,.85) 0%, transparent 100%),
      radial-gradient(ellipse 55% 30% at 50% 60%, var(--flame-orange) 0%, rgba(243,113,34,.75) 45%, transparent 100%),
      radial-gradient(ellipse 75% 40% at 50% 62%, rgba(236,31,39,.8) 0%, transparent 100%),
      radial-gradient(ellipse 80% 12% at 50% 86%, rgba(243,113,34,.7) 0%, transparent 100%),
      radial-gradient(ellipse 70% 10% at 50% 10%, rgba(243,113,34,.35) 0%, transparent 100%),
      linear-gradient(180deg, var(--ember-dark) 0%, var(--ember-deep) 22%, var(--ember-mid) 50%, var(--ember-deep) 88%, var(--ember-dark) 100%);
  }
  .front-cover .fire-art {
    background:
      radial-gradient(ellipse 18% 14% at 50% 42%, var(--glow-light) 0%, rgba(251,237,34,.8) 45%, transparent 100%),
      radial-gradient(ellipse 18% 14% at 18% 70%, rgba(251,237,34,.85) 0%, transparent 100%),
      radial-gradient(ellipse 18% 14% at 84% 70%, rgba(251,237,34,.8) 0%, transparent 100%),
      radial-gradient(ellipse 60% 32% at 50% 58%, var(--flame-orange) 0%, rgba(243,113,34,.75) 45%, transparent 100%),
      radial-gradient(ellipse 80% 42% at 50% 58%, rgba(236,31,39,.8) 0%, transparent 100%),
      radial-gradient(ellipse 80% 10% at 50% 27%, rgba(243,113,34,.55) 0%, transparent 100%),
      radial-gradient(ellipse 70% 10% at 50% 6%, rgba(243,113,34,.5) 0%, transparent 100%),
      linear-gradient(180deg, var(--ember-dark) 0%, var(--ember-deep) 20%, var(--ember-mid) 50%, var(--ember-deep) 88%, var(--ember-dark) 100%);
  }

  /* Back cover */
  .back-cover { position: relative; width: 533px; height: 100%; overflow: hidden; color: var(--ink-white); }
  .back-heading {
    position: absolute; top: 46px; width: 100%; text-align: center;
    font-size: 26px; font-weight: 500;
  }
  .back-summary {
    position: absolute; left: 33px; top: 107px; width: 451px;
    font-size: 12.3px; line-height: 21.5px; text-align: justify;
  }
  .publisher-mark {
    position: absolute; top: 548px; left: 0; width: 456px;
    text-align: center;
  }
  .publisher-dot {
    width: 40px; height: 40px; border-radius: 50%;
    background: var(--flame-orange); margin: 0 auto 14px;
  }
  .publisher-name { font-size: 19px; font-weight: 500; letter-spacing: 1px; line-height: 1.2; color: var(--ink-white); }
  .back-website {
    position: absolute; top: 700px; left: 0; width: 460px; text-align: center;
    font-size: 19px;
  }

  /* Spine */
  .spine {
    position: relative; width: 53px; height: 100%;
    background: linear-gradient(90deg, #1e0404, #4a0c08 50%, #1e0404);
    border-left: 1px solid rgba(0,0,0,.5); border-right: 1px solid rgba(0,0,0,.5);
  }
  .spine-title, .spine-author {
    position: absolute; left: 50%; white-space: nowrap;
    font-family: "Teko", sans-serif; font-weight: 600; line-height: 1;
    transform-origin: left top;
    transform: rotate(90deg) translateY(-50%);
  }
  .spine-title {
    top: 72px; font-size: 38px; color: var(--flame-yellow);
    text-shadow: 0 0 2px var(--flame-red), 1px 1px 0 var(--flame-orange), -1px -1px 0 var(--flame-orange);
  }
  .spine-author {
    top: 500px; font-size: 30px; color: var(--flame-orange);
    text-shadow: 1px 0 0 var(--ink-white), -1px 0 0 var(--ink-white), 0 1px 0 var(--ink-white), 0 -1px 0 var(--ink-white);
  }

  /* Front cover */
  .front-cover { position: relative; width: 534px; height: 100%; overflow: hidden; color: var(--ink-white); }
  .front-title {
    position: absolute; top: 34px; left: 0; width: 100%; text-align: center;
    font-family: "Teko", sans-serif; font-weight: 600; font-size: 56px; line-height: 1;
    color: var(--flame-yellow);
    transform: scaleX(.86);
    text-shadow: 0 2px 0 var(--flame-red), 0 0 12px rgba(243,113,34,.9);
  }
  .front-tagline {
    position: absolute; left: 67px; top: 88px; width: 430px;
    font-size: 15px; line-height: 18.5px;
  }
  .author-photo {
    position: absolute; left: 156px; top: 241px; width: 235px; height: 400px;
    border-radius: 90px 90px 0 0;
    background:
      linear-gradient(90deg, transparent 44%, var(--shirt-blue) 44%, var(--shirt-blue) 56%, transparent 56%) 0 120px / 100% 280px no-repeat,
      linear-gradient(180deg, #3a4a6e 0%, var(--suit-navy) 40%, var(--suit-shadow) 100%);
    box-shadow: 0 0 30px rgba(0,0,0,.35);
  }
  .front-author {
    position: absolute; top: 622px; left: 0; width: 100%; text-align: center;
    font-family: "Teko", sans-serif; font-weight: 600; font-size: 92px; line-height: 1;
    color: var(--flame-orange);
    transform: scaleX(.74);
    text-shadow: 2px 0 0 var(--ink-white), -2px 0 0 var(--ink-white), 0 2px 0 var(--ink-white), 0 -2px 0 var(--ink-white),
                 2px 2px 0 var(--ink-white), -2px -2px 0 var(--ink-white), 2px -2px 0 var(--ink-white), -2px 2px 0 var(--ink-white);
  }
</style>
</head>
<body>
  <main class="cover-spread">
    <section class="back-cover">
      <div class="fire-art" role="img" aria-label="Fiery explosion of yellow and orange flames bursting on a dark red background"></div>
      <h2 class="back-heading">Ownership, Vision and Action</h2>
      <p class="back-summary">Lorem ipsum dolor sit amet, consectetuer adipiscing elit, sed diam nonummy nibh euismod tincidunt ut laoreet dolore magna aliquam erat volutpat. Ut wisi enim ad minim veniam, quis nostrud exerci tation ullamcorper suscipit lobortis nisl ut aliquip ex ea commodo consequat. Duis autem vel eum iriure dolor in hendrerit in vulputate velit esse molestie consequat, Lorem ipsum dolor sit amet, consectetuer adipiscing elit, sed diam nonummy nibh euismod tincidunt ut laoreet dolore magna aliquam erat volutpat. Ut wisi enim ad minim veniam, quis nostrud exerci tation ullamcorper suscipit lobortis nisl ut aliquip ex ea commodo consequat. Duis autem vel eum iriure dolor in hendrerit in vulputate velit esse molestie consequat,</p>
      <div class="publisher-mark">
        <div class="publisher-dot"></div>
        <p class="publisher-name">THE<br>SUMMIT COLLECTIVE</p>
      </div>
      <p class="back-website">www.marlonteague-example.com</p>
    </section>

    <section class="spine">
      <span class="spine-title">RADIANT CROSSROADS</span>
      <span class="spine-author">MARLON TEAGUE</span>
    </section>

    <section class="front-cover">
      <div class="fire-art" role="img" aria-label="Fiery explosion of yellow and orange flames bursting behind the author"></div>
      <h1 class="front-title">RADIANT CROSSROADS</h1>
      <p class="front-tagline">Three Simple Steps to get out of your own way, SuperCharge your Life and Step into Purpose!</p>
      <div class="author-photo" role="img" aria-label="Photo of the author smiling in a navy blazer and light blue shirt"></div>
      <p class="front-author">MARLON TEAGUE</p>
    </section>
  </main>
</body>
</html>
```